Goal Planning Work Sheet

Design a better Goal Planning Worksheet that is fillable

Target Market(s)

People looking to make an important change

Industry/Entity Type

Work

Requirements
Must have
• Fillable pdf form
• Exceptional Design

```html
<!DOCTYPE html>
<html lang="en">
<head>
<meta charset="utf-8">
<title>I'm Being SMARTER Now – Goal Planning Worksheet</title>
<link rel="stylesheet" href="https://fonts.googleapis.com/css2?family=PT+Sans:wght@400;700&display=swap">
<style>
  :root {
    --backdrop: #58585a;
    --sidebar: #a8dde9;
    --sheet: #ffffff;
    --edge-tint: #b3e2ed;
    --heading-bar: #1b8ea6;
    --title-navy: #1d4a8a;
    --body-text: #3a4656;
    --bullet: #1d4a8a;
  }
  * { box-sizing: border-box; margin: 0; padding: 0; }
  html, body {
    width: 1200px; height: 907px; overflow: hidden;
    background: var(--backdrop);
    font-family: "PT Sans", Verdana, sans-serif;
  }
  .worksheet {
    position: absolute; left: 68px; top: 55px;
    width: 1064px; height: 798px;
    background: linear-gradient(90deg, var(--sheet) 0, var(--sheet) 79%, var(--edge-tint) 100%);
  }
  .sidebar {
    position: absolute; left: 0; top: 0;
    width: 205px; height: 100%;
    background: var(--sidebar);
  }
  .sidebar__title {
    position: absolute; left: 0; top: 8px; width: 205px;
    text-align: center; color: var(--title-navy);
    font-weight: 700; font-size: 25px; line-height: 27px; letter-spacing: .5px;
  }
  .sidebar__emblem {
    position: absolute; left: 54px; top: 98px;
    width: 94px; height: 94px;
  }
  .guide {
    position: absolute; left: 11px; width: 190px;
    color: var(--body-text); font-size: 10.4px; line-height: 13.4px;
  }
  .guide__heading {
    color: var(--title-navy); font-weight: 700; font-size: 12.6px;
    line-height: 15px; margin-bottom: 2px;
  }
  .guide__list { list-style: none; }
  .guide__list li { position: relative; padding-left: 14px; }
  .guide__list li::before {
    content: ""; position: absolute; left: 2px; top: 5px;
    width: 4px; height: 4px; border-radius: 50%; background: var(--bullet);
  }
  .guide__list b { color: #16233a; }
  .guide--strengths { top: 211px; }
  .guide--dare { top: 431px; }
  .guide--fear { top: 516px; }
  .guide--process { top: 622px; }

  .prompt {
    position: absolute; left: 205px; height: 24px;
    padding: 0 11px; background: var(--heading-bar);
    color: #fff; font-weight: 700; font-size: 13.2px; line-height: 24px;
    white-space: nowrap;
  }
  .prompt--vision { top: 20px; }
  .prompt--goal { top: 138px; }
  .prompt--obstacles { top: 388px; }
  .prompt--team { top: 551px; }
  .prompt--review { top: 669px; }
</style>
</head>
<body>
<main class="worksheet">
  <aside class="sidebar">
    <h1 class="sidebar__title">I'M BEING<br>SMARTER<br>NOW</h1>
    <svg class="sidebar__emblem" viewBox="0 0 94 94" role="img" aria-label="Compass with a heart at its centre">
      <defs>
        <radialGradient id="emblemFill" cx="45%" cy="40%" r="60%">
          <stop offset="0" stop-color="#e6f6fa"/>
          <stop offset="1" stop-color="#7cc4d6"/>
        </radialGradient>
      </defs>
      <circle cx="47" cy="47" r="46" fill="url(#emblemFill)"/>
    </svg>

    <section class="guide guide--strengths">
      <h2 class="guide__heading">Strength Spotting</h2>
      <ul class="guide__list">
        <li><b>Wisdom:</b> Cognitive Creativity Curiosity Judgment Love of Learning Perspective</li>
        <li><b>Courage:</b> Bravery Perseverance Honesty Zest</li>
        <li><b>Humanity:</b> Love Kindness Social Intelligence Teamwork</li>
        <li><b>Justice:</b> Fairness Leadership</li>
        <li><b>Temperance:</b> Forgiveness Humility Prudence Self-Regulation</li>
        <li><b>Transcendence:</b> Appreciation Beauty &amp; Excellence Gratitude Hope Humor Spirituality</li>
      </ul>
    </section>

    <section class="guide guide--dare">
      <h2 class="guide__heading">DARE</h2>
      <ul class="guide__list">
        <li>Fuse To Thoughts and Feelings</li>
        <li>Excessive Thinking</li>
        <li>Attractors Negative Emotional</li>
        <li>Run Away &amp; Avoidance</li>
      </ul>
    </section>

    <section class="guide guide--fear">
      <h2 class="guide__heading">FEAR</h2>
      <ul class="guide__list">
        <li><b>Defuse:</b> Notice, Name, Normalize</li>
        <li><b>Acceptance:</b> Allow, Appreciate Reinforce Skills &amp; Support Enjoy Values</li>
      </ul>
    </section>

    <section class="guide guide--process">
      <h2 class="guide__heading">Problem Solving Process</h2>
      <ul class="guide__list">
        <li>Domain of Problem</li>
        <li>Team Gathered</li>
        <li>Values Focus</li>
        <li>Imagine, Move, Be</li>
        <li>Define Problem, Cause,</li>
        <li>Solutions</li>
        <li>Plan-SMARTER Goals</li>
        <li>Resources &amp; Resourcefulness</li>
        <li>Practice, Rehearse</li>
        <li>Act Communicate</li>
        <li>Evaluate Revise</li>
      </ul>
    </section>
  </aside>

  <h2 class="prompt prompt--vision">Imagine and Move (motion creates emotion) Being the person I want to be, Values, Character Strengths:</h2>
  <h2 class="prompt prompt--goal">Specific Small Meaningful Measurable Actionable Attainable Timeline Now:</h2>
  <h2 class="prompt prompt--obstacles">Roadblocks Resources Rewards Ramification:</h2>
  <h2 class="prompt prompt--team">Team Roles:</h2>
  <h2 class="prompt prompt--review">Evaluate, Emotions, Revise, Resilient</h2>
</main>
</body>
</html>
```